Business Card design for a skin clinic

i would like a business card design for our skin clinic.
our logo colors are Blue and Grey and Bule /white.
we are searching for a minimalistic design yet very elegant,dynamic and professional which can reflect a professional medical skin care clinic( not a beauty salon).
THE DESGIN IS NOT FOR A PERSON IT WILL BE USED IN THE CLINIC FOR CLIENTS SO THERE SHOULD BE NO NAME OF A PERSON ONLY THE CLINIC NAME AND THE CONTACT INFO

Target Market(s)
young and old womens
Industry/Entity Type
Business
Contact Information for Business Card
we have 2 address and both should be on the card.
address A: Lindenhofkade 42B, 3017KP Rotterdam, Tel 010 438 21 95
address B: Zonnewijzerstraat 73, 1062HT Amsterdam Tel 020 519 8372
website www.velorahuid.nu, email info@velorahuid.nu
Look and feel

```html
<!DOCTYPE html>
<html lang="nl">
<head>
<meta charset="utf-8">
<title>Velora Huid – Visitekaartje</title>
<link href="https://fonts.googleapis.com/css2?family=Encode+Sans+Condensed:wght@300;400&display=swap" rel="stylesheet">
<style>
  :root {
    --page-bg: #f4f4f4;
    --card-bg: #ffffff;
    --brand-blue: #3a8fd6;
    --brand-grey: #6b6b6b;
    --ink: #1f1f1f;
    --ghost: #ececec;
  }
  * { margin: 0; padding: 0; box-sizing: border-box; }
  html, body {
    width: 1200px; height: 1200px; overflow: hidden;
    background: var(--page-bg);
    font-family: "Encode Sans Condensed", "Arial Narrow", sans-serif;
  }
  .canvas { position: relative; width: 1200px; height: 1200px; }
  .card {
    position: absolute; left: 203px; width: 794px; height: 520px;
    background: var(--card-bg);
  }
  .card--front { top: 66px; }
  .card--back { top: 616px; }

  .brand {
    position: absolute; left: 0; right: 0; top: 230px;
    text-align: center;
  }
  .brand__name {
    font-weight: 400; font-size: 46px; letter-spacing: 6px;
    color: var(--brand-blue); line-height: 1;
  }
  .brand__tagline {
    margin-top: 16px; font-weight: 300; font-size: 16px;
    letter-spacing: 3px; color: var(--brand-grey);
  }

  .ghost-name {
    position: absolute; left: 0; right: 0; top: 260px;
    text-align: center; font-weight: 400; font-size: 46px;
    letter-spacing: 6px; color: var(--ghost); line-height: 1;
  }
  .contact {
    position: absolute; top: 364px; width: 300px;
    text-align: center; color: var(--ink);
    font-weight: 300; font-size: 21px; line-height: 28px; letter-spacing: 0.4px;
  }
  .contact--rotterdam { left: 97px; }
  .contact--amsterdam { left: 395px; }
  .contact__online {
    margin-top: 10px; display: flex; align-items: center; justify-content: center; gap: 6px;
  }
  .contact__icon { width: 24px; height: 20px; }
</style>
</head>
<body>
<main class="canvas">
  <section class="card card--front">
    <div class="brand">
      <div class="brand__name">VELORA HUID</div>
      <div class="brand__tagline">next generation skin care</div>
    </div>
  </section>

  <section class="card card--back">
    <div class="ghost-name" aria-hidden="true">VELORA HUID</div>

    <address class="contact contact--rotterdam" style="font-style:normal">
      Lindenhofkade 42B,<br>
      3017KP Rotterdam,<br>
      P: 010 438 21 95
      <div class="contact__online">
        <svg class="contact__icon" viewBox="0 0 24 24" fill="none" stroke="var(--ink)" stroke-width="1.2" aria-hidden="true">
          <circle cx="11" cy="11" r="9"/>
          <ellipse cx="11" cy="11" rx="4" ry="9"/>
          <line x1="2" y1="11" x2="20" y2="11"/>
          <line x1="3.5" y1="6.5" x2="18.5" y2="6.5"/>
          <line x1="3.5" y1="15.5" x2="18.5" y2="15.5"/>
          <path d="M16 16 L22 19 L19 20 L18 23 Z" fill="var(--ink)"/>
        </svg>
        <span>www.velorahuid.nu</span>
      </div>
    </address>

    <address class="contact contact--amsterdam" style="font-style:normal">
      Zonnewijzerstraat 73,<br>
      1062HT Amsterdam<br>
      P: 020 519 8372
      <div class="contact__online">
        <svg class="contact__icon" viewBox="0 0 26 20" fill="none" stroke="var(--ink)" stroke-width="1.3" aria-hidden="true">
          <rect x="1" y="2" width="24" height="16"/>
          <path d="M1 2 L13 12 L25 2"/>
          <path d="M1 18 L10 9.5 M25 18 L16 9.5"/>
        </svg>
        <span>info@velorahuid.nu</span>
      </div>
    </address>
  </section>
</main>
</body>
</html>
```